Business Card Design Project

See the detainl of the Vortel company project I also have live: http://tasks.quillmarsh.com/task.aspx?id=382917

Reason: I am waiting to select a logo design and ideally the business card design will be from the same person

Industry/Entity Type

Business

```html
<!DOCTYPE html>
<html lang="en">
<head>
<meta charset="utf-8">
<title>Corvane LLP – Business Card</title>
<link rel="stylesheet" href="https://fonts.googleapis.com/css2?family=Lato:wght@400;700;900&display=swap">
<style>
  :root {
    --backdrop: #2b2b2d;
    --card-top: #ffffff;
    --card-bottom: #e8e9ea;
    --brand-blue: #1ba3dc;
    --ink: #1a1a1a;
    --ink-soft: #2a2a2a;
    --label-text: #ffffff;
  }
  * { box-sizing: border-box; margin: 0; padding: 0; }
  html, body {
    width: 1200px;
    height: 900px;
    overflow: hidden;
  }
  body {
    background: var(--backdrop);
    font-family: "Lato", Arial, sans-serif;
    color: var(--ink);
    position: relative;
  }
  .card {
    position: absolute;
    left: 100px;
    top: 160px;
    width: 1000px;
    height: 580px;
    border-radius: 34px;
    background: linear-gradient(160deg, var(--card-top) 0%, var(--card-top) 45%, var(--card-bottom) 100%);
    box-shadow: 0 24px 60px rgba(0,0,0,0.55);
  }
  .brand {
    position: absolute;
    top: 72px;
    left: 0;
    width: 100%;
    display: flex;
    justify-content: center;
    align-items: center;
    gap: 14px;
  }
  .brand-mark {
    width: 22px;
    height: 22px;
    background: var(--brand-blue);
    flex: none;
  }
  .brand-name {
    font-weight: 700;
    font-size: 46px;
    color: var(--brand-blue);
    text-transform: uppercase;
    line-height: 1;
  }
  .divider {
    position: absolute;
    left: 478px;
    top: 170px;
    width: 5px;
    height: 340px;
    background: linear-gradient(180deg, rgba(27,163,220,0) 0%, var(--brand-blue) 25%, var(--brand-blue) 70%, rgba(27,163,220,0) 100%);
  }
  .person {
    position: absolute;
    right: 560px;
    top: 250px;
    text-align: right;
  }
  .person-name {
    font-weight: 900;
    font-size: 38px;
    color: var(--brand-blue);
    text-transform: uppercase;
    line-height: 1.05;
  }
  .person-role {
    font-weight: 700;
    font-size: 26px;
    color: var(--ink);
    margin-top: 2px;
  }
  .office-label {
    display: inline-block;
    margin-top: 34px;
    padding: 2px 12px;
    background: var(--brand-blue);
    color: var(--label-text);
    font-weight: 400;
    font-size: 28px;
    letter-spacing: 0.5px;
    text-transform: uppercase;
  }
  .office-address {
    font-weight: 700;
    font-size: 27px;
    line-height: 1.3;
    margin-top: 6px;
    color: var(--ink-soft);
  }
  .partnership {
    font-weight: 700;
    font-size: 28px;
    margin-top: 28px;
    color: var(--ink-soft);
  }
  .partnership-number { color: var(--brand-blue); }
  .contact {
    position: absolute;
    left: 520px;
    top: 192px;
  }
  .site-address {
    font-weight: 900;
    font-size: 25px;
    line-height: 1.25;
    color: var(--ink);
  }
  .contact-list {
    list-style: none;
    margin-top: 18px;
  }
  .contact-item {
    display: flex;
    align-items: center;
    gap: 20px;
    font-weight: 700;
    font-size: 28px;
    line-height: 1;
    height: 46px;
    color: var(--ink-soft);
  }
  .contact-icon {
    width: 28px;
    height: 28px;
    flex: none;
    fill: var(--brand-blue);
  }
  .website {
    font-weight: 900;
    font-size: 26px;
    margin-top: 12px;
    margin-left: 48px;
    color: var(--ink);
  }
  .website-domain { color: var(--brand-blue); }
</style>
</head>
<body>
  <main class="card">
    <header class="brand">
      <span class="brand-mark" aria-hidden="true"></span>
      <span class="brand-name">Corvane LLP</span>
    </header>

    <div class="divider"></div>

    <section class="person">
      <div class="person-name">Your Name</div>
      <div class="person-role">Centre Director</div>
      <div class="office-label">Registered Office:</div>
      <div class="office-address">Alder House, 9B Mill Lane,<br>Harlow, HR1 4LP</div>
      <div class="partnership">Partnership No. <span class="partnership-number">OC512046</span></div>
    </section>

    <section class="contact">
      <div class="site-address">14 Harlow Research Park<br>Fenwick Road, Harlow, HR2 7QA</div>
      <ul class="contact-list">
        <li class="contact-item">
          <svg class="contact-icon" viewBox="0 0 28 28" aria-hidden="true">
            <path d="M3 10c0-4 5-6 11-6s11 2 11 6v2h-6v-3h-10v3H3z"/>
            <path d="M7 14h14l3 9H4z"/>
          </svg>
          <span>+44 (0)1632 960481</span>
        </li>
        <li class="contact-item">
          <svg class="contact-icon" viewBox="0 0 28 28" aria-hidden="true">
            <path d="M8 2h12a2 2 0 0 1 2 2v20a2 2 0 0 1-2 2H8a2 2 0 0 1-2-2V4a2 2 0 0 1 2-2zm1 4v14h10V6zm5 16a1.5 1.5 0 1 0 0 .01z" fill-rule="evenodd"/>
          </svg>
          <span>+44 (0)7700 900XXX</span>
        </li>
        <li class="contact-item">
          <svg class="contact-icon" viewBox="0 0 28 28" aria-hidden="true">
            <path d="M8 3h12v6H8z"/>
            <path d="M3 11h22v10h-4v-4H7v4H3z"/>
            <path d="M8 19h12v6H8z"/>
          </svg>
          <span>(0)1632 960482</span>
        </li>
        <li class="contact-item">
          <svg class="contact-icon" viewBox="0 0 28 28" aria-hidden="true">
            <path d="M2 6h24v16H2zm2 2v1l10 7 10-7V8z" fill-rule="evenodd"/>
          </svg>
          <span>tom.reade@corvane.co.uk</span>
        </li>
      </ul>
      <div class="website">www.<span class="website-domain">corvane</span>.co.uk</div>
    </section>
  </main>
</body>
</html>
```